VELDA Metals - newly established Metal trading business

Velda Metals is a newly established Metal trading, processing and refining business

we are looking for a simple and professional business website, which is easy to navigate

We will be selling metal / commodities to some of the largest industrial business globally. Therefore the website must make us look like a large and reputable business.

We have attached a Powerpoint presentation with some ideas

Target Market(s)

Lagre metal consumers

Industry/Entity Type

Commodity

Logo Text

VELDA Metals Group

Coding

Coded - Design and coding required

Number of Pages Required

5+ page

Font styles to use
Sans Serif

Colors

Designer to choose colors to be used in the design.

Requirements
Must have
• - fixed menu bar at the top
• - continuous scroll down function
• - multiple tabs left and right for more information
• - have dynamic screen size adjustment / a mobile version
• - google maps

```html
<!DOCTYPE html>
<html lang="en">
<head>
<meta charset="utf-8">
<title>VELDA Metals Group</title>
<link rel="stylesheet" href="https://fonts.googleapis.com/css2?family=Montserrat:wght@300;400;500;600;700&family=Noto+Serif:ital,wght@0,400;0,700;1,400&display=swap">
<style>
:root{
  --ink:#2b2f3a;
  --body:#6d7380;
  --muted:#9aa0aa;
  --violet:#5b3fd2;
  --violet-soft:#7b62e0;
  --blue:#1f9ad6;
  --navy:#1e2a5a;
  --paper:#ffffff;
  --mist:#eef0f3;
  --mist-dark:#e3e6eb;
  --footer:#dfe3ea;
  --icon:#3d7fc4;
}
*{box-sizing:border-box;margin:0;padding:0}
html,body{width:1200px;height:4972px;overflow:hidden}
body{font-family:"Noto Serif",Georgia,serif;color:var(--body);background:var(--paper);font-size:12px;line-height:1.7}
section,footer{position:relative;width:1200px;overflow:hidden}
.abs{position:absolute}
.center{text-align:center}
h1,h2,h3,h4{font-family:"Montserrat",Arial,sans-serif;font-weight:500;color:var(--ink)}
.btn{display:inline-block;font-family:"Montserrat",Arial,sans-serif;font-size:9px;letter-spacing:2px;text-transform:uppercase;font-weight:600;white-space:nowrap}
.btn-outline{border:1px solid var(--ink);color:var(--ink);padding:7px 18px;background:#fff}
.btn-violet{border:1px solid var(--violet);color:var(--violet);padding:7px 18px;background:#fff}
.btn-blue{background:var(--blue);color:#fff;padding:9px 26px;border-radius:20px}
.link{font-family:"Montserrat",Arial,sans-serif;font-size:9px;letter-spacing:2px;color:var(--violet);font-weight:600;text-transform:uppercase}
.icon{width:38px;height:38px;flex:none;stroke:var(--icon);fill:none;stroke-width:1.6;stroke-linecap:round;stroke-linejoin:round}
.fill{position:absolute}

/* Top bar */
.topbar{position:absolute;z-index:5;top:0;left:0;width:1200px;height:64px;display:flex;align-items:center;justify-content:space-between;padding:0 60px;background:rgba(30,42,90,.18)}
.brand{display:flex;align-items:center;gap:10px;font-family:"Montserrat",Arial,sans-serif;font-weight:600;font-size:16px;color:#fff;letter-spacing:.5px}
.brand i{display:block;width:14px;height:14px;background:#fff}
.menu{display:flex;gap:30px;font-family:"Montserrat",Arial,sans-serif;font-size:10px;letter-spacing:2px;text-transform:uppercase;color:#fff;font-weight:500}

/* Hero */
.hero{height:590px;background:linear-gradient(180deg,#c9ced6 0%,#dfe3e9 45%,#cfd4dc 100%)}
.hero-title{position:absolute;top:170px;left:0;width:100%;text-align:center;color:#fff;font-size:38px;font-weight:400;line-height:1.3}
.play{position:absolute;top:300px;left:565px;width:70px;height:70px;border-radius:50%;background:var(--blue)}
.hero-text{position:absolute;top:412px;left:410px;width:380px;text-align:center;color:#5d6470;font-size:11px;font-style:italic}

/* Split features */
.split{height:510px;background:var(--mist)}
.split-photo{left:484px;top:50px;width:230px;height:415px;background:linear-gradient(160deg,#d5d8dd,#8e949c 60%,#c2c6cc)}
.feat{position:absolute;width:230px;text-align:center}
.feat h4{font-size:13px;margin:8px 0 6px}
.feat p{font-size:11px}

/* Phone section */
.phones{height:500px;background:linear-gradient(100deg,#f4f5f7 0%,#e7e9ed 55%,#f4f5f7 100%)}
.phones-art{left:630px;top:65px;width:250px;height:335px;background:linear-gradient(135deg,#f4f4f6,#d9dbe0 55%,#2c2e33 56%,#46484e)}
.step{position:absolute;left:330px;width:290px;display:flex;gap:14px}
.step h4{font-size:14px;margin-bottom:4px}
.step p{font-size:10px}

/* Services */
.services{height:505px;background:#fff}
.eyebrow{font-family:"Montserrat",Arial,sans-serif;font-size:9px;letter-spacing:3px;color:var(--violet-soft);text-transform:uppercase}
.services h2{font-size:26px;color:var(--violet);font-weight:600}
.card{position:absolute;top:125px;width:238px;height:310px;text-align:center;padding-top:40px}
.card-bg{position:absolute;inset:0;background:linear-gradient(180deg,#eceef1,#dcdfe4 60%,#f0f1f3)}
.card-inner{position:relative}
.card h4{font-size:15px;margin:12px 0 10px}
.card p{font-size:11px;width:180px;margin:0 auto 26px}

/* Visualization */
.visual{height:530px;background:#fff;border-top:1px solid var(--mist-dark)}
.visual h2{font-size:34px;font-weight:300;color:var(--violet)}
.col4{position:absolute;display:flex;left:260px;width:680px}
.col4 > div{flex:1;text-align:center;padding:0 12px}
.col4 h4{font-size:12px;margin:10px 0 8px}
.col4 p{font-size:10px}

/* World */
.world{height:495px;background:linear-gradient(180deg,#eef1f5 0%,#d7dde6 55%,#e9ecf0 100%)}
.world h2{font-size:34px;font-weight:300;color:var(--violet-soft)}

/* Showcase */
.showcase{height:595px;background:var(--mist)}
.panel{position:absolute;background:#fff;padding:44px 40px}
.panel h3{font-size:20px;font-weight:600;color:var(--navy);margin-bottom:14px}
.panel p{font-size:11px;margin-bottom:16px}

/* Contact */
.contact{height:500px;background:#f5f6f8}
.contact-card{position:absolute;left:238px;top:42px;width:722px;height:410px;background:#fff}
.contact h3{font-size:22px;font-weight:600;color:var(--navy)}
.cline{display:flex;align-items:flex-start;gap:12px;font-size:11px;margin-bottom:16px}
.cline svg{flex:none;margin-top:2px}
.map{left:368px;top:10px;width:344px;height:390px;background:linear-gradient(135deg,#eef0e8,#dde4d6 40%,#e8ebe4 70%,#f2f0ea)}

/* Features */
.features{height:515px;background:#fff}
.features h2{font-size:26px;font-weight:600;color:var(--navy)}
.fgrid{position:absolute;left:238px;top:140px;width:724px;display:grid;grid-template-columns:repeat(3,1fr);row-gap:30px}
.fgrid div{display:flex;align-items:center;gap:14px;font-family:"Montserrat",Arial,sans-serif;font-size:10px;letter-spacing:1.5px;text-transform:uppercase;color:var(--ink)}
.social{position:absolute;top:450px;left:272px;display:flex;gap:8px}
.social span{width:126px;height:32px;display:flex;align-items:center;justify-content:center;color:#fff;font-family:"Montserrat",Arial,sans-serif;font-size:9px;letter-spacing:1.5px;text-transform:uppercase;font-weight:600}

/* Footer */
.site-footer{height:232px;background:var(--footer)}
.fcol{position:absolute;top:56px;width:150px}
.fcol h4{font-size:14px;color:var(--navy);margin-bottom:12px}
.fcol a{display:block;font-family:"Montserrat",Arial,sans-serif;font-size:9px;letter-spacing:1.5px;color:var(--violet-soft);text-transform:uppercase;text-decoration:none;line-height:2.1}
</style>
</head>
<body>

<section class="hero">
  <div class="fill" style="inset:0" role="img" aria-label="Upward view of glass office towers against a pale sky"></div>
  <nav class="topbar">
    <div class="brand"><i></i>VELDA Metals Group</div>
    <div class="menu"><span>Home</span><span>About</span><span>Metals</span><span>Services</span><span>Contact</span></div>
  </nav>
  <h1 class="hero-title">Great Styling For Headers<br>And Hero Images</h1>
  <div class="play">
    <svg width="70" height="70" viewBox="0 0 70 70"><path d="M29 24 L47 35 L29 46 Z" fill="#fff"/></svg>
  </div>
  <p class="hero-text">Velda Metals trades, processes and refines metals for the largest industrial buyers, with steady supply on every shipment.</p>
  <svg class="abs" style="left:586px;top:540px" width="30" height="8"><circle cx="4" cy="4" r="3" fill="#fff"/><circle cx="15" cy="4" r="3" fill="#fff" opacity=".5"/><circle cx="26" cy="4" r="3" fill="#fff" opacity=".5"/></svg>
</section>

<section class="split">
  <div class="fill split-photo" role="img" aria-label="Office desk seen from above with a laptop and a person at work"></div>
  <div class="feat" style="left:266px;top:52px">
    <svg class="icon" viewBox="0 0 40 40"><circle cx="20" cy="20" r="14"/><path d="M13 20 L18 25 L27 15"/></svg>
    <h4>Easy with Metals</h4>
    <p>We move bulk copper, steel and alloys with ease. Every lot is graded and shipped on time to your plant.</p>
  </div>
  <div class="feat" style="left:266px;top:255px">
    <svg class="icon" viewBox="0 0 40 40"><path d="M8 32 L22 18"/><path d="M22 18 L32 8"/><path d="M28 32 L12 16"/><circle cx="10" cy="12" r="4"/></svg>
    <h4>Construction Grade</h4>
    <p>Beams, plate and rebar cut to your plans, tested and certified so each piece fits your site.</p>
  </div>
  <div class="feat" style="left:732px;top:52px">
    <svg class="icon" viewBox="0 0 40 40"><circle cx="20" cy="20" r="6"/><path d="M20 6v6M20 28v6M6 20h6M28 20h6M10 10l4 4M26 26l4 4M30 10l-4 4M14 26l-4 4"/></svg>
    <h4>Fabrication</h4>
    <p>From raw coil to finished part, our lines give you one trusted source for every stage.</p>
  </div>
  <div class="feat" style="left:732px;top:255px">
    <svg class="icon" viewBox="0 0 40 40"><rect x="8" y="10" width="24" height="20" rx="2"/><path d="M8 17h24M15 10v20"/></svg>
    <h4>Wrought Iron</h4>
    <p>Wrought iron made to last and easy to fit, so your project moves ahead without delay.</p>
  </div>
</section>

<section class="phones">
  <div class="fill" style="inset:0;opacity:.6" role="img" aria-label="Faded photo of a bright office interior"></div>
  <div class="step" style="top:60px">
    <svg class="icon" viewBox="0 0 40 40"><circle cx="20" cy="20" r="14"/><path d="M14 22l4 4 8-10"/></svg>
    <div><h4>Strategy &amp; Planning</h4><p>Every lot, route and contract is planned with care to keep your supply steady.</p></div>
  </div>
  <div class="step" style="top:165px">
    <svg class="icon" viewBox="0 0 40 40"><circle cx="20" cy="20" r="14"/><path d="M20 12v8l6 4"/></svg>
    <div><h4>Design &amp; Development</h4><p>Choose from a wide range of grades and finishes, then order by your specs.</p></div>
  </div>
  <div class="step" style="top:270px">
    <svg class="icon" viewBox="0 0 40 40"><circle cx="20" cy="20" r="14"/><path d="M13 20h14M22 15l5 5-5 5"/></svg>
    <div><h4>Release &amp; Marketing</h4><p>Fast delivery with clear tracking and paperwork, so every load arrives on cue.</p></div>
  </div>
  <div class="fill phones-art" role="img" aria-label="Two smartphones showing the Velda Metals website"></div>
</section>

<section class="services">
  <p class="eyebrow center abs" style="top:62px;width:100%">Features &amp; Services</p>
  <h2 class="center abs" style="top:78px;width:100%">Services We Can Help You With</h2>
  <div class="card" style="left:242px">
    <div class="card-bg" role="img" aria-label="Faded photo of an engineer's desk"></div>
    <div class="card-inner">
      <svg class="icon" viewBox="0 0 40 40"><rect x="7" y="9" width="26" height="18" rx="1"/><path d="M15 33h10M20 27v6"/></svg>
      <h4>Fabrication</h4>
      <p>Bring us your drawings and we cut, bend and weld each part to spec.</p>
      <span class="btn btn-violet">Find out more</span>
    </div>
  </div>
  <div class="card" style="left:487px">
    <div class="card-bg" role="img" aria-label="Faded photo of hands on a keyboard"></div>
    <div class="card-inner">
      <svg class="icon" viewBox="0 0 40 40"><rect x="9" y="8" width="22" height="24" rx="1"/><path d="M14 15h12M14 20h12M14 25h8"/></svg>
      <h4>Development</h4>
      <p>We source and refine new alloys so your plant always gets the right stock.</p>
      <span class="btn btn-violet">Find out more</span>
    </div>
  </div>
  <div class="card" style="left:733px">
    <div class="card-bg" role="img" aria-label="Faded photo of a tablet on a table"></div>
    <div class="card-inner">
      <svg class="icon" viewBox="0 0 40 40"><path d="M8 28V12h24v16H8z"/><path d="M8 12l12 9 12-9"/></svg>
      <h4>Consulting</h4>
      <p>Talk with our metal experts about pricing, risk and supply for your firm.</p>
      <span class="btn btn-violet">Find out more</span>
    </div>
  </div>
</section>

<section class="visual">
  <h2 class="center abs" style="top:48px;width:100%">Construction Visualization Visually</h2>
  <p class="center abs" style="top:104px;left:420px;width:360px;font-size:11px">From ore to finished stock, we show every step of the supply chain so you can plan with confidence.</p>
  <div class="col4" style="top:180px">
    <div><svg class="icon" viewBox="0 0 40 40"><path d="M10 10l8 20 3-8 8-3z"/></svg><h4>Select &amp; Edit</h4><p>Pick grades, sizes and finishes from our range and we prepare each order.</p></div>
    <div><svg class="icon" viewBox="0 0 40 40"><rect x="8" y="10" width="24" height="20" rx="1"/><path d="M8 16h24M14 22h4M22 22h4"/></svg><h4>No Skills Required</h4><p>Small lots or full vessels, our team handles testing, customs and freight.</p></div>
    <div><svg class="icon" viewBox="0 0 40 40"><circle cx="20" cy="22" r="11"/><path d="M20 22l5-5M17 8h6"/></svg><h4>Speed Is the Key</h4><p>Stock held in key ports means short lead times for every major market.</p></div>
    <div><svg class="icon" viewBox="0 0 40 40"><rect x="10" y="14" width="20" height="16" rx="1"/><path d="M14 14V8h12v6M10 21h20"/></svg><h4>Easy to Use</h4><p>One account manager, clear contracts and simple terms for your buyers.</p></div>
  </div>
  <span class="btn btn-outline abs" style="left:540px;top:400px">Get a quote</span>
</section>

<section class="world">
  <div class="fill" style="inset:0;opacity:.5" role="img" aria-label="Faded photo of a red suspension bridge"></div>
  <h2 class="center abs" style="top:45px;width:100%">Beautiful world</h2>
  <p class="center abs" style="top:96px;left:400px;width:400px;font-size:11px">Velda Metals serves industrial buyers on every continent with steady supply, fair pricing and full traceability.</p>
  <span class="btn btn-blue abs" style="left:525px;top:160px">More about us</span>
  <div class="col4" style="top:290px">
    <div><svg class="icon" viewBox="0 0 40 40"><circle cx="20" cy="20" r="6"/><circle cx="20" cy="20" r="13"/></svg><h4>Focus Groups</h4><p>Dedicated desks for steel, copper, aluminium and precious metals.</p></div>
    <div><svg class="icon" viewBox="0 0 40 40"><rect x="8" y="12" width="24" height="18" rx="1"/><path d="M14 12V8h12v4"/></svg><h4>Pressure Sensitive</h4><p>Hedging and fixed pricing protect you from sudden market swings.</p></div>
    <div><svg class="icon" viewBox="0 0 40 40"><rect x="12" y="7" width="16" height="26" rx="2"/><path d="M18 29h4"/></svg><h4>Smartwatch Ready</h4><p>Live prices and shipment alerts on any screen, wherever you are.</p></div>
    <div><svg class="icon" viewBox="0 0 40 40"><rect x="9" y="8" width="22" height="24" rx="2"/><path d="M15 16h10M15 22h10"/></svg><h4>Perfect On Mobiles</h4><p>Track orders, certificates and invoices from your phone.</p></div>
  </div>
</section>

<section class="showcase">
  <div class="fill" style="left:298px;top:51px;width:232px;height:232px;background:linear-gradient(150deg,#f6f6f4,#d9a066 45%,#8a5a34 75%,#eceae6)" role="img" aria-label="Ornate orange armchair in a bright room"></div>
  <div class="panel" style="left:547px;top:51px;width:353px;height:232px">
    <h3>Gorgeous Design</h3>
    <p>Our refined metals meet strict international standards. Each batch is assayed, certified and packed for safe transport to your plant.</p>
    <span class="link">View more</span>
  </div>
  <div class="panel" style="left:315px;top:310px;width:348px;height:221px">
    <h3>Comfortable Options</h3>
    <p>Spot, term and tolling contracts let you buy the way that suits your business. Flexible terms, with one partner.</p>
    <span class="link">View more</span>
  </div>
  <div class="fill" style="left:680px;top:310px;width:220px;height:221px;background:linear-gradient(150deg,#f2f2f2,#c9c9cb 40%,#5b1820 60%,#e8e8e8)" role="img" aria-label="Wine bottle and glasses on a white table"></div>
</section>

<section class="contact">
  <div class="contact-card">
    <div class="abs" style="left:0;top:14px;width:340px">
      <h3>Contact Info</h3>
      <p style="font-size:11px;margin:14px 0 26px;width:220px">Speak with our trading desk about supply, pricing and delivery. We reply within one business day.</p>
      <div class="cline"><svg width="16" height="16" viewBox="0 0 16 16"><path d="M8 15s5-5 5-8.5A5 5 0 0 0 3 6.5C3 10 8 15 8 15z" fill="var(--icon)"/><circle cx="8" cy="6.5" r="1.8" fill="#fff"/></svg><span>14 Orden Lane Marlow, 06210<br>Vermont, USA</span></div>
      <div class="cline"><svg width="16" height="16" viewBox="0 0 16 16"><path d="M4 2l3 3-1.5 2a8 8 0 0 0 3.5 3.5L11 9l3 3-2 2C7 14 2 9 2 4z" fill="var(--icon)"/></svg><span>+41 55 20 18</span></div>
      <div class="cline"><svg width="16" height="16" viewBox="0 0 16 16"><circle cx="8" cy="8" r="7" fill="var(--icon)"/><path d="M4.5 6l3.5 3 3.5-3" stroke="#fff" fill="none"/></svg><span>sales@veldametals.com</span></div>
    </div>
    <div class="fill map" role="img" aria-label="Street map with a red pin marking the Velda Metals office"></div>
  </div>
</section>

<section class="features">
  <h2 class="abs" style="left:238px;top:58px">Our Great Features</h2>
  <p class="abs" style="left:646px;top:50px;width:314px;font-size:11px">Velda Metals combines global sourcing, in-house refining and reliable logistics to serve the world's largest industrial buyers.</p>
  <div class="fgrid">
    <div><svg class="icon" viewBox="0 0 40 40"><circle cx="20" cy="22" r="11"/><path d="M20 22l5-5"/></svg>Fast loading time</div>
    <div><svg class="icon" viewBox="0 0 40 40"><circle cx="20" cy="20" r="6"/><path d="M20 6v6M20 28v6M6 20h6M28 20h6"/></svg>Hundreds of options</div>
    <div><svg class="icon" viewBox="0 0 40 40"><path d="M20 6l12 5v8c0 8-6 13-12 15C14 32 8 27 8 19v-8z"/></svg>Security preferences</div>
    <div><svg class="icon" viewBox="0 0 40 40"><path d="M7 10h5l4 16h14l3-11H14"/><circle cx="17" cy="31" r="2"/><circle cx="28" cy="31" r="2"/></svg>Store Commerce</div>
    <div><svg class="icon" viewBox="0 0 40 40"><path d="M8 10h24v16H18l-6 5v-5H8z"/></svg>Active support</div>
    <div><svg class="icon" viewBox="0 0 40 40"><rect x="10" y="8" width="20" height="24" rx="1"/><path d="M10 16h20M10 24h20"/></svg>Database access</div>
    <div><svg class="icon" viewBox="0 0 40 40"><path d="M5 20s6-9 15-9 15 9 15 9-6 9-15 9S5 20 5 20z"/><circle cx="20" cy="20" r="4"/></svg>Intuitive builder</div>
    <div><svg class="icon" viewBox="0 0 40 40"><rect x="8" y="8" width="24" height="24"/><path d="M8 20h24M20 8v24"/></svg>Premade skins</div>
    <div><svg class="icon" viewBox="0 0 40 40"><path d="M14 12l-8 8 8 8M26 12l8 8-8 8"/></svg>Coding freedom</div>
  </div>
  <p class="eyebrow center abs" style="top:410px;width:100%">Follow us on social</p>
  <div class="social">
    <span style="background:#c9222b">Pinwall</span>
    <span style="background:#3b5493">Facelink</span>
    <span style="background:#1d9fe0">Chirper</span>
    <span style="background:#7c3aa8">Snapgram</span>
    <span style="background:#222">Folioworks</span>
  </div>
</section>

<footer class="site-footer">
  <div class="fcol" style="left:298px"><h4>Links</h4><a>Home</a><a>About us</a><a>Portfolio</a><a>Blog</a></div>
  <div class="fcol" style="left:454px"><h4>Contact</h4><a>Send message</a><a>Contact us</a><a>Live chat</a><a>Phone call</a></div>
  <div class="fcol" style="left:610px"><h4>Address</h4><a>14 Orden Lane</a><a>Marlow, 06210</a><a>Vermont</a></div>
  <div class="fcol" style="left:765px"><h4>Follow us on:</h4>
    <svg width="60" height="12"><circle cx="5" cy="6" r="4" fill="var(--violet-soft)"/><circle cx="20" cy="6" r="4" fill="var(--violet-soft)"/><circle cx="35" cy="6" r="4" fill="var(--violet-soft)"/></svg>
  </div>
</footer>

</body>
</html>
```